Lantern Advisory Website

I currently have a website www.lanternadvisoryinc.example. We are a IT Consulting Company. Our website will pretty much tell out our services. I am looking to enhance my website and make it look more professional. Looking for very classy and Contemporary look and design for my website.

It Company

```html
<!DOCTYPE html>
<html lang="en">
<head>
<meta charset="utf-8">
<title>Lantern Advisory</title>
<link href="https://fonts.googleapis.com/css2?family=Raleway:wght@300;400;600;700&family=Open+Sans:ital,wght@0,400;0,600;1,400&display=swap" rel="stylesheet">
<style>
:root{
  --blue:#0e9fd9;
  --blue-deep:#1a5fa6;
  --navy:#164a80;
  --ink:#222831;
  --grey:#555c66;
  --mist:#e9edf1;
  --line:#c9d0d8;
  --white:#ffffff;
}
*{margin:0;padding:0;box-sizing:border-box}
html,body{width:672px;height:1200px;overflow:hidden;background:var(--white)}
body{font-family:"Open Sans",Arial,sans-serif;color:var(--ink)}
.page{position:relative;width:672px;height:1200px;overflow:hidden}
.abs{position:absolute}

/* header */
.topbar{left:0;top:0;width:672px;height:2px;background:var(--blue)}
.header{left:0;top:2px;width:672px;height:48px;background:linear-gradient(#f7f8f9,#e8ebee)}
.brand{left:60px;top:16px;display:flex;align-items:center;gap:6px}
.brand-mark{width:16px;height:16px;background:var(--blue-deep)}
.brand-name{font-family:"Raleway",sans-serif;font-weight:700;font-size:14px;color:var(--blue-deep);letter-spacing:.3px;white-space:nowrap}
.contact-item{top:13px;display:flex;align-items:center;gap:7px}
.contact-icon{width:19px;height:19px;border-radius:50%;background:var(--blue-deep);display:flex;align-items:center;justify-content:center}
.contact-label{font-family:"Raleway",sans-serif;font-weight:700;font-size:6.5px;color:var(--blue-deep)}
.contact-value{font-size:7.5px;color:var(--grey);white-space:nowrap}

/* nav */
.nav{left:0;top:50px;width:672px;height:23px;background:linear-gradient(#1aa7e0,#0b7fc0)}
.nav ul{list-style:none;display:flex;margin-left:60px;height:23px}
.nav li{font-family:"Raleway",sans-serif;font-weight:700;font-size:7.5px;color:var(--white);display:flex;align-items:center;justify-content:center;border-right:1px solid rgba(0,0,0,.12)}
.nav li.active{background:var(--blue)}

/* hero */
.hero{left:0;top:73px;width:672px;height:229px;background:radial-gradient(circle at 68% 45%,#6f8fb0 0%,#2c4766 35%,#16263c 70%,#0f1a2a 100%)}
.hero-title{left:60px;top:72px;width:300px;font-family:"Raleway",sans-serif;font-weight:700;font-size:13px;line-height:18.5px;color:var(--white)}
.btn-more{left:60px;top:140px;width:69px;height:23px;background:var(--blue);color:var(--white);font-family:"Raleway",sans-serif;font-weight:700;font-size:7px;display:flex;align-items:center;padding-left:12px;clip-path:polygon(0 0,88% 0,100% 30%,100% 100%,0 100%)}

/* welcome */
.welcome{left:0;top:302px;width:672px;height:107px;background:linear-gradient(#14a6df,#0c92cf)}
.welcome-title{top:10px;width:672px;text-align:center;font-family:"Raleway",sans-serif;font-weight:300;font-size:17.5px;color:var(--white)}
.welcome-rule{left:200px;top:37px;width:272px;height:1px;background:rgba(255,255,255,.5)}
.welcome-text{left:66px;top:48px;width:540px;text-align:center;font-size:7.3px;line-height:12px;color:rgba(255,255,255,.88)}
.plus{left:324px;top:94px;width:24px;height:13px;background:#2f3338;color:var(--white);font-weight:600;font-size:11px;line-height:13px;text-align:center}

/* features */
.feature{top:440px;width:170px;text-align:center}
.feature-title{margin-top:94px;font-family:"Raleway",sans-serif;font-weight:700;font-size:9.5px;color:var(--ink)}
.feature.highlight .feature-title{color:var(--blue)}
.feature-text{margin-top:6px;font-size:7.2px;line-height:9.6px;color:var(--grey)}

/* services */
.services{left:0;top:609px;width:672px;height:179px;background:var(--mist)}
.section-title{width:672px;text-align:center;font-family:"Raleway",sans-serif;font-weight:400;font-size:17.5px;color:var(--ink)}
.section-title span{color:var(--blue)}
.section-rule{left:250px;width:172px;height:1px;background:var(--line)}
.section-dot{left:331px;width:9px;height:9px;background:var(--blue-deep)}
.card{top:61px;width:165px;height:94px}
.card-photo{position:absolute;inset:0}
.card-label{position:absolute;left:0;bottom:0;width:100%;height:19px;background:rgba(16,80,150,.85);color:var(--white);font-family:"Raleway",sans-serif;font-size:10px;text-align:center;line-height:19px}
.card-feature{background:#1f66a8;padding:14px 16px 0;text-align:center;color:var(--white)}
.card-feature h3{font-family:"Raleway",sans-serif;font-weight:700;font-size:10px}
.card-feature p{margin-top:6px;font-weight:600;font-size:6.4px;line-height:9.4px}
.card-feature .more{margin-top:5px;font-weight:700;font-size:6px}

/* testimonial */
.quote{left:166px;top:853px;width:446px;font-style:italic;font-size:7.3px;line-height:13.5px;color:var(--grey);text-align:center}
.quote-rule{left:166px;top:918px;width:446px;height:1px;background:#e2e6ea}
.quote-name{left:222px;top:929px;font-weight:600;font-size:7px;color:var(--blue-deep)}
.portrait{left:70px;top:858px;width:80px;height:80px;border-radius:50%;border:3px solid #d4d8dc;background:radial-gradient(circle at 50% 40%,#c9a58b 0%,#8a6d5c 35%,#2e3a4f 75%)}
.dots{left:523px;top:930px;display:flex;gap:3px}
.dots i{width:5px;height:5px;border-radius:50%;background:#c7ccd1}
.dots i:first-child{background:var(--blue)}

/* footer */
.footer{left:0;top:1000px;width:672px;height:175px;background:var(--blue-deep)}
.footer-col{top:1031px}
.footer-col h4{font-family:"Raleway",sans-serif;font-weight:600;font-size:10px;line-height:12px;color:var(--white);white-space:nowrap}
.footer-col ul{list-style:none;margin-top:13px}
.footer-col li{font-size:6.7px;color:var(--white);margin-bottom:13.5px}
.links li::before{content:"";display:inline-block;width:2.5px;height:2.5px;background:var(--white);margin-right:6px;vertical-align:middle}
.info-row{display:flex;gap:8px;font-size:6.7px;line-height:9px;color:var(--white);margin-bottom:12px}
.info-row svg{flex:none;margin-top:1px}
.divider{top:1040px;width:1px;height:110px;background:rgba(0,0,0,.15)}
.field{width:150px;height:19px;border:1px solid rgba(255,255,255,.6);margin-top:5px;font-size:6.7px;color:var(--white);padding:4px 6px}
.field.tall{height:34px}
.submit{margin-top:8px;width:58px;height:18px;background:linear-gradient(#fff,#dfe3e7);color:var(--ink);font-size:7.5px;text-align:center;line-height:18px;border-radius:2px}
.footer-brand{left:500px;top:1065px;display:flex;align-items:center;gap:6px}
.footer-brand .brand-mark{background:var(--white)}
.footer-brand .brand-name{color:var(--white);font-size:11px}
.social{left:504px;top:1114px;display:flex;gap:8px}
.social i{width:17px;height:17px;background:rgba(255,255,255,.85)}
.copyright{left:0;top:1175px;width:672px;height:25px;background:var(--navy);color:var(--white);font-size:6.7px;text-align:center;line-height:25px}
</style>
</head>
<body>
<div class="page">

  <div class="abs topbar"></div>
  <header class="abs header">
    <div class="abs brand" style="top:14px">
      <span class="brand-mark"></span>
      <span class="brand-name">LANTERN ADVISORY</span>
    </div>
    <div class="abs contact-item" style="left:374px">
      <span class="contact-icon"><svg width="8" height="10" viewBox="0 0 8 10"><rect x="1" y="0.5" width="6" height="9" rx="1" fill="none" stroke="#fff"/><rect x="2.5" y="2" width="3" height="4" fill="#fff"/></svg></span>
      <div><div class="contact-label">CALL US</div><div class="contact-value">+1 (555) 014 2290</div></div>
    </div>
    <div class="abs contact-item" style="left:475px">
      <span class="contact-icon"><svg width="10" height="8" viewBox="0 0 10 8"><rect x="0.5" y="0.5" width="9" height="7" fill="none" stroke="#fff"/><path d="M0.5 0.5 5 4.5 9.5 0.5" fill="none" stroke="#fff"/></svg></span>
      <div><div class="contact-label">EMAIL US</div><div class="contact-value">info@lanternadvisoryinc.example</div></div>
    </div>
  </header>

  <nav class="abs nav">
    <ul>
      <li class="active" style="width:62px">HOME</li>
      <li style="width:84px">ABOUT US</li>
      <li style="width:78px">SERVICES</li>
      <li style="width:84px">SOLUTIONS</li>
      <li style="width:86px">RESOURCES</li>
      <li style="width:72px">CAREER</li>
      <li style="width:86px;border-right:0">CONTACT US</li>
    </ul>
  </nav>

  <section class="abs hero" role="img" aria-label="Photo of a hand touching glowing technology gears">
    <h1 class="abs hero-title">DELIVERS HIGHEST LEVEL OF QUALITY CONSULTANTS AND SERVICES FOR THE LOWEST COST OF OWNERSHIP</h1>
    <div class="abs btn-more">READ MORE</div>
  </section>

  <section class="abs welcome">
    <h2 class="abs welcome-title">Welcome To Lantern Advisoryinc</h2>
    <div class="abs welcome-rule"></div>
    <svg class="abs" style="left:330px;top:37px" width="12" height="5"><path d="M0 0 6 5 12 0Z" fill="#fff"/></svg>
    <p class="abs welcome-text">Today's IT market is a dynamic, fast-paced industry, with ever-increasing demands. Meeting these demands for over 25 years, Lantern Advisory maintains a global presence, aggressively recruiting expertly qualified IT and Management Professionals from around the world and cultivating key partnerships with corporations to understand their business models end-to-end, with a goal of delivering exceptional client service and ensuring a consistent delivery....</p>
    <div class="abs plus">+</div>
  </section>

  <svg class="abs" style="left:0;top:430px" width="672" height="100">
    <g fill="none" stroke="#333" stroke-width="1">
      <path d="M141 17 149 10 157 17"/><path d="M141 88 149 95 157 88"/>
      <path d="M116 44 108 53 116 62"/><path d="M182 44 190 53 182 62"/>
      <path d="M518 17 526 10 534 17"/><path d="M518 88 526 95 534 88"/>
      <path d="M493 44 485 53 493 62"/><path d="M559 44 567 53 559 62"/>
    </g>
    <g fill="none" stroke="#0e9fd9" stroke-width="1">
      <path d="M335 10 343 17 351 10"/><path d="M335 84 343 77 351 84"/>
      <path d="M303 44 311 53 303 62"/><path d="M383 44 375 53 383 62"/>
    </g>
    <g fill="#222831">
      <circle cx="142" cy="44" r="3"/><circle cx="156" cy="44" r="3"/>
      <rect x="139" y="49" width="20" height="4"/>
      <rect x="138" y="54" width="4" height="9"/><rect x="156" y="54" width="4" height="9"/>
      <rect x="145" y="46" width="8" height="12"/>
    </g>
    <g transform="translate(343 53)">
      <circle r="9" fill="#0e9fd9"/>
      <g fill="#0e9fd9"><rect x="-2.5" y="-13" width="5" height="26"/><rect x="-13" y="-2.5" width="26" height="5"/><rect x="-2.5" y="-13" width="5" height="26" transform="rotate(45)"/><rect x="-2.5" y="-13" width="5" height="26" transform="rotate(-45)"/></g>
      <circle r="4" fill="#fff"/>
    </g>
    <rect x="515" y="42" width="22" height="22" rx="4" fill="#222831"/>
  </svg>

  <div class="abs feature" style="left:65px">
    <div class="feature-title">CONSULTING</div>
    <p class="feature-text">Lantern Advisory has certified professional consultants to work with you to help increase the business by providing IT services ...</p>
  </div>
  <div class="abs feature highlight" style="left:258px">
    <div class="feature-title">STAFF AUGMENTATION</div>
    <p class="feature-text">For years Lantern Advisory as been offering our customers the ability to augment their existing staff..</p>
  </div>
  <div class="abs feature" style="left:442px">
    <div class="feature-title">OFFSHORE</div>
    <p class="feature-text">Our Offshore development model has a unique distinction of providing efficient software solutions ...</p>
  </div>

  <section class="abs services">
    <h2 class="abs section-title" style="top:11px">Our <span>Services</span></h2>
    <div class="abs section-rule" style="top:38px"></div>
    <div class="abs section-dot" style="top:34px"></div>
    <svg class="abs" style="left:28px;top:67px" width="16" height="30"><path d="M15 1 1 15 15 29" fill="none" stroke="#8a939c"/></svg>
    <svg class="abs" style="left:624px;top:67px" width="16" height="30"><path d="M1 1 15 15 1 29" fill="none" stroke="#8a939c"/></svg>
    <div class="abs card" style="left:60px">
      <div class="card-photo" role="img" aria-label="Photo of a businessman touching floating technology icons" style="background:radial-gradient(circle at 50% 35%,#5a7a9a,#1c2a3c 70%)"></div>
      <div class="card-label">Technology</div>
    </div>
    <div class="abs card card-feature" style="left:253px">
      <h3>OFFSHORE</h3>
      <p>Our Offshore development model has a unique distinction of providing efficient software solutions with cost and quality advantage, using state-of-the-art</p>
      <div class="more">READ MORE »</div>
    </div>
    <div class="abs card" style="left:447px">
      <div class="card-photo" role="img" aria-label="Photo of a person touching application icons on a screen" style="background:radial-gradient(circle at 40% 40%,#8fd0ee,#2a8fc4 55%,#14527f)"></div>
      <div class="card-label">Application Development</div>
    </div>
  </section>

  <section>
    <h2 class="abs section-title" style="top:806px">Client <span>Testimonial</span></h2>
    <div class="abs section-rule" style="top:834px"></div>
    <div class="abs section-dot" style="top:830px"></div>
    <div class="abs portrait" role="img" aria-label="Portrait photo of the client"></div>
    <svg class="abs" style="left:151px;top:853px" width="10" height="9"><path d="M0 9V4L3 0H5L3 4H4V9ZM5 9V4L8 0H10L8 4H9V9Z" fill="#b5bcc3"/></svg>
    <p class="abs quote">Lorem ipsum dolor sit amet, consectetuer adipiscing elit, sed diam nonummy nibh euismod tincidunt utvm laoreetm dolore magna aliquam erat volutpat. Ut wisi enim ad minim veniam, quis nostrud exerci tation ullamcorper suscipit lobortis nisl utmv aliquip ex ea commodo consequat. Duis autem vel eum iriure dolor in hendrerit in vulputate velit esse molestie consequat, velm illu dolore eu feugiat nulla facilisis at vero eros et accumsan etsto duis facilisi.</p>
    <svg class="abs" style="left:494px;top:897px" width="10" height="9"><path d="M10 0V5L7 9H5L7 5H6V0ZM5 0V5L2 9H0L2 5H1V0Z" fill="#b5bcc3"/></svg>
    <div class="abs quote-rule"></div>
    <svg class="abs" style="left:250px;top:918px" width="8" height="5"><path d="M0 0 4 5 8 0Z" fill="#d6dbe0"/></svg>
    <div class="abs quote-name">- Miss Clara Penning</div>
    <div class="abs dots"><i></i><i></i><i></i><i></i></div>
  </section>

  <svg class="abs" style="left:0;top:920px" width="672" height="82">
    <path d="M672 0C590 50 480 82 360 80C310 79 280 76 260 74C470 92 590 60 672 22Z" fill="#0ea8e6"/>
    <path d="M0 80C70 40 170 30 260 52C340 72 400 82 460 80C560 76 620 50 672 28V82H0Z" fill="#1a5fa6"/>
  </svg>

  <footer class="abs footer"></footer>
  <div class="abs footer-col links" style="left:60px">
    <h4>Quick Links</h4>
    <ul><li>Home</li><li>About Us</li><li>Services</li><li>Resources</li><li>Contact Us</li></ul>
  </div>
  <div class="abs divider" style="left:134px"></div>
  <div class="abs footer-col" style="left:159px">
    <h4>Contact Information</h4>
    <div style="margin-top:12px">
      <div class="info-row"><svg width="7" height="9" viewBox="0 0 7 9"><path d="M3.5 9C1 5.5 0 4.5 0 3.3A3.5 3.5 0 0 1 7 3.3C7 4.5 6 5.5 3.5 9Z" fill="#fff"/><circle cx="3.5" cy="3.3" r="1.2" fill="#1a5fa6"/></svg><span>418 Harbor Row<br>Suite 12<br>Easton Ridge, NJ 07999</span></div>
      <div class="info-row"><svg width="7" height="7" viewBox="0 0 7 7"><path d="M1 0 3 2 2 3C2.5 4 3 4.5 4 5L5 4 7 6 6 7C3 7 0 4 0 1Z" fill="#fff"/></svg><span>+1 (555) 014 2290</span></div>
      <div class="info-row"><svg width="8" height="7" viewBox="0 0 8 7"><rect x="2" y="0" width="4" height="2" fill="#fff"/><rect x="0" y="2.5" width="8" height="3" fill="#fff"/><rect x="2" y="5" width="4" height="2" fill="#fff"/></svg><span>555.010.7745</span></div>
      <div class="info-row"><svg width="7" height="6" viewBox="0 0 7 6"><rect width="7" height="6" fill="#fff"/><path d="M0 0 3.5 3 7 0" fill="none" stroke="#1a5fa6"/></svg><span>hello@mailbox.example</span></div>
    </div>
  </div>
  <div class="abs divider" style="left:281px"></div>
  <div class="abs footer-col" style="left:305px">
    <h4>Quick Contact</h4>
    <div style="margin-top:5px">
      <div class="field">Name</div>
      <div class="field">Phone</div>
      <div class="field tall">Message</div>
      <div class="submit">SUBMIT</div>
    </div>
  </div>
  <div class="abs divider" style="left:475px"></div>
  <div class="abs footer-brand"><span class="brand-mark"></span><span class="brand-name">LANTERN ADVISORY</span></div>
  <div class="abs social"><i></i><i></i><i></i><i></i></div>

  <div class="abs copyright">Copyright © 2016 Lanternadvisoryinc. All Rights Reserved.</div>
</div>
</body>
</html>
```